Take an existing presentation and make it more dynamic and professional.

We have an existing powerpoint presentation that we are using both as a presentation tool and also with a voice over on Youtube.

Content is pretty much there. Needs a new theme that is modern and contemporary.

Can answer questions regarding all slides as we have added a few new ones in just for this project.

Can also provide links to the youtube vid so you understand what voice over depicts in regards to the presentation

More relevant graphics may need to be use to create a uniform feel throughout the presentation.

We are looking for an awesome designer who really knows power point to create something truly spectacular. In most cases this will be the first presentation that someone sees of our company so it must be exactly right.

You can watch the Youtube video here. http://vidnest.example/QTRWX8KZp2

Target Market(s)

People seeking to start a business. We are offering an opportunity to partner with us in a lucrative business model which has low start up costs but very quick financial rewards over the first 3 months. The products are back by 25 years of scientific research and 100% of the people that use them they work on.

Industry/Entity Type

It Company

Font styles to use
Sans Serif

Colors
0492cd
33a6d7
85cae6
cee9f5
ebf7f9
0255a3

Requirements
Must have
• Modern professional clean look. Good transitions, Relevant images.
• First slide title, logo and background to stay unless you come up with a better background.
• Colors should be blues.
• Slide with the bottles should have new better looking graphics. All 8 bottles should be pointing to s single bottle in the centre. A theme that we can apply to our other presentations. Though if the project turns out the way we hope we will provide the contest winner with our other presentations to fix.
Nice to have
• Some slides can be combined.
Should not have
• Images that do not fit with the theme, anything that distracts from the message of the slides both text and images should be complementary.

```html
<!DOCTYPE html>
<html lang="en">
<head>
<meta charset="utf-8">
<title>Conventional Business Model</title>
<link href="https://fonts.googleapis.com/css2?family=Roboto+Condensed:wght@400;700;900&display=swap" rel="stylesheet">
<style>
  :root {
    --sky-top: #0d6bd6;
    --sky-mid: #2c93ea;
    --sky-bottom: #62c2f4;
    --band-dark: #0255a3;
    --band-fade: rgba(4, 146, 205, 0);
    --white: #ffffff;
    --highlight: #b4ecff;
    --faint: rgba(2, 85, 163, 0.28);
    --stamp: rgba(2, 85, 163, 0.22);
    --source: #0a4f9a;
  }
  * { margin: 0; padding: 0; box-sizing: border-box; }
  html, body { width: 1200px; height: 900px; overflow: hidden; }
  body { font-family: "Roboto Condensed", "Arial Narrow", sans-serif; }

  .slide {
    position: relative;
    width: 1200px;
    height: 900px;
    overflow: hidden;
    background: linear-gradient(180deg, var(--sky-top) 0%, var(--sky-mid) 45%, var(--sky-bottom) 100%);
  }

  .title-band {
    position: absolute;
    left: 0; top: 0;
    width: 100%; height: 93px;
    background: linear-gradient(90deg, var(--band-dark) 0%, rgba(2, 85, 163, 0.75) 45%, var(--band-fade) 100%);
    border-bottom: 2px solid rgba(255, 255, 255, 0.08);
  }
  .slide-title {
    position: absolute;
    left: 18px; top: 20px;
    font-size: 46px;
    font-weight: 400;
    color: var(--white);
    letter-spacing: 0.2px;
  }

  .points { position: absolute; left: 40px; top: 150px; width: 1120px; list-style: none; }
  .point {
    position: relative;
    padding-left: 54px;
    font-size: 33px;
    line-height: 56px;
    color: var(--white);
    margin-bottom: 48px;
  }
  .tick { position: absolute; left: 0; top: 14px; width: 36px; height: 30px; }
  .label { font-weight: 900; color: var(--highlight); letter-spacing: 0.5px; }
  .strong { font-weight: 700; color: var(--highlight); }

  .stat-backdrop {
    position: absolute;
    left: 196px; top: 540px;
    font-size: 198px;
    font-weight: 900;
    color: var(--faint);
    line-height: 1;
    letter-spacing: -4px;
  }

  .stamp-area {
    position: absolute;
    left: 612px; top: 380px;
    width: 500px; height: 500px;
    border-radius: 50%;
    background: radial-gradient(circle, rgba(2, 85, 163, 0.16) 0%, var(--stamp) 70%, rgba(2, 85, 163, 0.08) 100%);
  }

  .source {
    position: absolute;
    left: 0; right: 0; top: 862px;
    text-align: center;
    font-size: 21px;
    color: var(--source);
    letter-spacing: 0.5px;
  }
</style>
</head>
<body>
<main class="slide">
  <header class="title-band">
    <h1 class="slide-title">Conventional Business Model</h1>
  </header>

  <ul class="points">
    <li class="point">
      <svg class="tick" viewBox="0 0 36 30" aria-hidden="true"><path d="M2 16 L12 26 L34 3" fill="none" stroke="#ffffff" stroke-width="6" stroke-linecap="round" stroke-linejoin="round"/></svg>
      <span class="label">CONVENTIONAL BIZ MODEL –</span> you develop everything yourself.<br>
      <span class="strong">80% of these businesses fail</span> in the first 5yrs*
    </li>
    <li class="point">
      <svg class="tick" viewBox="0 0 36 30" aria-hidden="true"><path d="M2 16 L12 26 L34 3" fill="none" stroke="#ffffff" stroke-width="6" stroke-linecap="round" stroke-linejoin="round"/></svg>
      <span class="label">FRANCHISING – <span class="strong">95% succeed</span></span>. You develop nothing. You get the<br>
      systems, product, branding &amp; training
    </li>
  </ul>

  <div class="stat-backdrop" aria-hidden="true">80%</div>
  <div class="stamp-area" role="img" aria-label="Faint rubber stamp illustration marked FAILED with stars around its edge"></div>

  <p class="source">*MARKETLEDGER</p>
</main>
</body>
</html>
```